Webdesign für Branchenverzeichnis
Zielgruppe
Wir-bauen-Brücken – das Branchenverzeichnis der Selbstverantwortlichen.
Der Anbieter präsentiert sich mit seinem Namen und der URL - ähnlich wie bei 'blaue Blätter' oder Torkwerk.
Aufgabenstellung
Das Branchenverzeichnis sollte neutral und gleichzeitig hochwertig sein. Die Hauptfarben sind Gold, Schwarz und Weiß. Logo und Corporate Design wurden bereits entwickelt

```html
<!DOCTYPE html>
<html lang="de">
<head>
<meta charset="utf-8">
<title>Wir bauen Brücken – Mitgliedschaft</title>
<link href="https://fonts.googleapis.com/css2?family=Quicksand:wght@400;500;600;700&display=swap" rel="stylesheet">
<style>
:root{
  --gold:#d3ae5e;
  --gold-soft:#e6d3a6;
  --ink:#111111;
  --text:#3e3e3e;
  --muted:#8a8a8a;
  --cream:#fffdf3;
  --white:#ffffff;
  --line:#dedede;
  --dark:#3f3f3f;
  --head-top:#2f2f2f;
  --head-bottom:#5c5c5c;
}
*{box-sizing:border-box;margin:0;padding:0}
html,body{width:1200px;height:934px;overflow:hidden}
body{font-family:'Quicksand',sans-serif;background:var(--cream);color:var(--text);position:relative}
.site-header{position:absolute;left:0;top:0;width:1200px;height:62px;background:linear-gradient(180deg,var(--head-top),var(--head-bottom))}
.brand{position:absolute;left:158px;top:13px;display:flex;align-items:center;gap:6px;color:var(--gold);font-weight:700;font-size:10px;line-height:1.1;width:90px}
.brand-dot{width:14px;height:14px;border-radius:50%;border:2px solid var(--gold);flex:none}
.main-nav a{position:absolute;top:25px;font-size:9px;font-weight:700;letter-spacing:1.2px;color:var(--white);text-decoration:none}
.main-nav a.active{color:var(--gold)}
.icon-box{position:absolute;top:19px;width:25px;height:25px;border:1px solid var(--gold);display:flex;align-items:center;justify-content:center}
.btn-join{position:absolute;left:919px;top:17px;width:125px;height:28px;background:var(--gold);color:var(--white);font-size:8px;font-weight:600;letter-spacing:.8px;display:flex;align-items:center;justify-content:center;border-radius:2px}
.intro{position:absolute;left:158px;top:150px;width:560px}
.intro h1{font-size:30px;font-weight:700;letter-spacing:1.5px;color:var(--ink);line-height:1.1}
.intro h1 span{color:var(--gold)}
.intro .subtitle{font-size:15px;font-weight:500;letter-spacing:.8px;color:var(--ink);margin-top:6px}
.intro p{font-size:11px;line-height:17px;letter-spacing:.6px;color:var(--muted);margin-top:14px;width:400px}
.intro h2{font-size:11px;font-weight:700;letter-spacing:.8px;color:var(--ink);margin-top:30px}
.steps p{color:var(--text);width:430px;margin-top:17px}
.steps p:first-child{margin-top:20px}
.signup{position:absolute;left:744px;top:113px;width:300px;height:489px;background:var(--white);border:1px solid var(--gold);box-shadow:0 2px 8px rgba(0,0,0,.06)}
.tabs{position:absolute;left:19px;top:12px;width:262px;height:12px}
.tabs span{position:absolute;top:0;font-size:11.5px;font-weight:500;color:var(--ink);letter-spacing:.4px}
.tab-line{position:absolute;left:18px;top:30px;width:262px;height:3px;background:#f0f0f0;border-radius:2px}
.tab-line::before{content:"";position:absolute;left:0;top:0;width:70px;height:3px;background:var(--gold);border-radius:2px}
.field{position:absolute;left:39px;width:219px;height:31px;border:1px solid var(--line);display:flex;align-items:center;justify-content:space-between;padding:0 12px;font-size:7.5px;color:#777}
.field svg{width:12px;height:12px}
.check{position:absolute;left:39px;display:flex;align-items:center;gap:10px;font-size:7.5px;color:#777}
.check i{width:12px;height:12px;border:1px solid var(--line);border-radius:2px}
.btn-buy{position:absolute;left:39px;top:431px;width:219px;height:31px;background:var(--dark);color:var(--white);font-size:8px;font-weight:600;letter-spacing:.7px;display:flex;align-items:center;justify-content:center;border-radius:2px}
.site-footer{position:absolute;left:0;top:661px;width:1200px;height:273px;background:linear-gradient(180deg,#6b6b6b,#3b3b3b);color:var(--gold)}
.footer-brand{position:absolute;left:256px;top:80px;display:flex;align-items:center;gap:6px;font-size:10px;font-weight:700;width:70px;line-height:1.2}
.footer-about{position:absolute;left:360px;top:80px;width:190px}
.footer-about h3{font-size:11.5px;font-weight:700;letter-spacing:.3px}
.footer-about p{font-size:9.5px;line-height:16px;margin-top:10px}
.footer-about a{display:block;font-size:9.5px;color:var(--gold);margin-top:6px}
.footer-col{position:absolute;top:78px}
.footer-col h4{font-size:11.5px;font-weight:700;letter-spacing:.8px}
.footer-col li{list-style:none;font-size:9.5px;margin-top:12px}
.footer-col li:first-child{margin-top:14px}
.copyright{position:absolute;left:0;width:1200px;top:240px;text-align:center;font-size:7.5px;font-weight:600;letter-spacing:.3px}
</style>
</head>
<body>
<header class="site-header">
  <div class="brand"><span class="brand-dot"></span>Wir bauen Brücken</div>
  <nav class="main-nav">
    <a style="left:287px">HOME</a>
    <a style="left:362px">SUCHEN</a>
    <a style="left:450px">ÜBER UNS</a>
    <a class="active" style="left:544px">MITGLIEDSCHAFT</a>
    <a style="left:675px">KONTAKT</a>
  </nav>
  <div class="icon-box" style="left:824px">
    <svg width="17" height="12" viewBox="0 0 17 12"><rect width="17" height="4" fill="#000"/><rect y="4" width="17" height="4" fill="#dd0000"/><rect y="8" width="17" height="4" fill="#ffce00"/></svg>
  </div>
  <div class="icon-box" style="left:856px">
    <svg width="12" height="12" viewBox="0 0 12 12" fill="#fff"><circle cx="6" cy="3.5" r="2.8"/><path d="M0.5 12c0-3.3 2.5-5 5.5-5s5.5 1.7 5.5 5z"/></svg>
  </div>
  <div class="btn-join">MITGLIED WERDEN</div>
</header>

<section class="intro">
  <h1>WIR ZEIGEN <span>DEIN UNTERNEHMEN</span></h1>
  <div class="subtitle">Das Branchenverzeichnis der Selbstverantwortlichen</div>
  <p>Lorem ipsum dolor sit amet, consectetur adipisicing elit, sed do eiusmod tempor incididunt ut labore et dolore magna aliqua. Duis aute irure dolor in reprehenderit in voluptate velit esse cillum dolore eu fugiat nulla pariatur. Ut enim ad minim veniam, quis nostrud</p>
  <h2>WIE WERDE ICH MITGLIED IN 3 EINFACHEN SCHRITTEN?</h2>
  <div class="steps">
    <p>1. Im Formular (rechts von dir) deine Daten eintragen und absenden</p>
    <p>2. Du wirst zu deiner Bank verbunden, um eine Banküberweisung zu tätigen. Für 200€ bekommst du eine Mitgliedschaft für 1 Jahr. Danach wirst du von uns automatisch 4 Wochen vor Ablauf deiner Mitgliedschaft benachrichtigt, ob du die Mitgliedschaft weiter führen möchtest.</p>
    <p>3. Du kannst dich nun mit deiner Email-Adresse und deinem Passwort in unserem Branchenverzeichnis einloggen und deinen eigenen Eintrag erstellen.</p>
  </div>
</section>

<form class="signup">
  <div class="tabs"><span style="left:0">Registrieren</span><span style="left:90px">Login</span></div>
  <div class="tab-line"></div>
  <div class="field" style="top:52px">Vor- und Nachname<svg viewBox="0 0 12 12" fill="var(--gold-soft)"><circle cx="6" cy="6" r="6"/><circle cx="6" cy="4.5" r="2" fill="#fff"/><path d="M2.5 10a4 3 0 0 1 7 0z" fill="#fff"/></svg></div>
  <div class="field" style="top:93px">Firmenname<svg viewBox="0 0 12 12" fill="none" stroke="var(--gold-soft)"><rect x="1" y="1" width="6" height="10"/><rect x="7" y="4" width="4" height="7"/></svg></div>
  <div class="field" style="top:133px">Firmenadresse eingeben<svg viewBox="0 0 12 12" fill="none" stroke="var(--gold-soft)" stroke-width="1.3"><circle cx="6" cy="6" r="4"/><circle cx="6" cy="6" r="1.5" fill="var(--gold-soft)"/><path d="M6 0v2M6 10v2M0 6h2M10 6h2"/></svg></div>
  <div class="field" style="top:174px">Email-Adresse<svg viewBox="0 0 12 12" fill="none" stroke="var(--gold-soft)" stroke-width="1.3"><circle cx="6" cy="6" r="2"/><path d="M8 6v1a1.8 1.8 0 0 0 3.5 0V6A5.5 5.5 0 1 0 9 10.5"/></svg></div>
  <div class="field" style="top:215px">Passwort<svg viewBox="0 0 12 12" fill="none" stroke="var(--gold-soft)" stroke-width="1.5"><path d="M1 6.5l3.2 3L11 2.5"/></svg></div>
  <div class="field" style="top:256px">Branche wählen<svg viewBox="0 0 12 12" fill="none" stroke="var(--gold)" stroke-width="1.5"><path d="M1 3.5l5 5 5-5"/></svg></div>
  <div class="field" style="top:296px">Paket: Mitgliedschaft für 1 Jahr (200€)<svg viewBox="0 0 12 12" fill="none" stroke="var(--gold-soft)" stroke-width="1.2"><rect x="0.6" y="2" width="10.8" height="8" rx="1"/><path d="M0.6 4.8h10.8" stroke-width="1.6"/></svg></div>
  <div class="field" style="top:337px">Bezahlung: Banküberweisung<svg viewBox="0 0 12 12" fill="none" stroke="var(--gold-soft)" stroke-width="1.2"><path d="M5 4h6M9 2l2 2-2 2M7 8H1M3 6L1 8l2 2"/></svg></div>
  <label class="check" style="top:382px"><i></i>Ich akzeptiere die DSGVO</label>
  <label class="check" style="top:401px"><i></i>Ich akzeptiere die AGB</label>
  <div class="btn-buy">MITGLIEDSCHAFT KAUFEN</div>
</form>

<footer class="site-footer">
  <div class="footer-brand"><span class="brand-dot"></span>Wir bauen Brücken</div>
  <div class="footer-about">
    <h3>Wir bauen Brücken</h3>
    <p>Duis sed odio sit amet nibh vulputate cursus a sit amet mauris. Morbi accumsan ipsum velit. Nam nec tellus a</p>
    <a>Über uns</a>
  </div>
  <div class="footer-col" style="left:647px">
    <h4>WEBSITE</h4>
    <ul><li>Wir bauen Brücken</li><li>Unternehmen suchen</li><li>Mitgliedschaft</li><li>Kontakt</li></ul>
  </div>
  <div class="footer-col" style="left:839px">
    <h4>RECHTLICHES</h4>
    <ul><li>Impressum</li><li>Datenschutz</li><li>AGB</li><li>Sicherheitsbestimmungen</li></ul>
  </div>
  <div class="copyright">© 2020 Wir Bauen Brücken</div>
</footer>
</body>
</html>
```